Harbor Vault Works Business Card Design

I would like someone to design a business card that is similar to the top design on the safes in the pictures. I like the curvature of the wording on the safes and I like the font and the scrolling from the Granite Western signs I sent. I would also like to incorporate king neptune/ posidon in the center of scroll above "Harbor Vault Works"

Target Market(s)

Gun Safes

Industry/Entity Type

Business

Contact Information for Business Card

The scrolling should be on the sides and throughout the "Harbor Vault Works" arching in the top of the card.

Font styles to use
Decorative

Colors

Designer to choose colors to be used in the design.

Requirements
Must have
• Scrolling, old school font
Nice to have
• some image of king neptune/ posidon in the scroll

```html
<!DOCTYPE html>
<html lang="en">
<head>
<meta charset="utf-8">
<title>Harbor Vault Works – Business Card</title>
<link rel="stylesheet" href="https://fonts.googleapis.com/css2?family=Cinzel:wght@400;700&family=Open+Sans:wght@400;600;700&display=swap">
<style>
  :root {
    --backdrop: #3a332e;
    --card: #0f0f0f;
    --accent-red: #e0201f;
    --text-white: #f2f2f2;
    --silver: #c4c4c4;
    --scroll-dark: #4a4a4a;
    --scroll-light: #a8a8a8;
    --divider: #3a3a3a;
  }
  * { margin: 0; padding: 0; box-sizing: border-box; }
  html, body { width: 1200px; height: 900px; overflow: hidden; }
  body {
    background: var(--backdrop);
    font-family: "Open Sans", Arial, sans-serif;
    position: relative;
  }
  .card {
    position: absolute;
    width: 520px;
    height: 300px;
    background: var(--card);
    box-shadow: 0 14px 30px rgba(0,0,0,.55);
  }
  .card-front { left: 50px; top: 310px; }
  .card-back  { left: 630px; top: 310px; }

  /* front */
  .front-brand {
    position: absolute;
    left: 30px; top: 0; bottom: 0;
    width: 235px;
    display: flex; align-items: center; gap: 12px;
  }
  .brand-dot {
    width: 14px; height: 14px; flex: none;
    background: var(--accent-red);
    border-radius: 50%;
  }
  .brand-name {
    color: var(--accent-red);
    font-family: "Cinzel", "Times New Roman", serif;
    font-weight: 700;
    font-size: 28px;
    line-height: 1.15;
    letter-spacing: 1px;
  }
  .front-divider {
    position: absolute;
    left: 276px; top: 56px; bottom: 56px;
    width: 1px; background: var(--divider);
  }
  .contact {
    position: absolute;
    left: 292px; top: 62px; right: 16px;
    color: var(--text-white);
    font-size: 13px;
    line-height: 1.4;
  }
  .contact-name {
    color: var(--accent-red);
    font-weight: 700;
    font-size: 18px;
    line-height: 1.2;
  }
  .contact-role { margin-bottom: 12px; }
  .contact-address { margin-bottom: 12px; }
  .contact-line { display: flex; align-items: center; gap: 8px; }
  .contact-line svg { width: 10px; height: 10px; flex: none; fill: var(--accent-red); }

  /* back */
  .back-lockup { position: absolute; inset: 0; }
  .back-lockup svg { width: 520px; height: 300px; display: block; }
  .back-name-arch {
    font-family: "Cinzel", "Times New Roman", serif;
    font-weight: 400;
    font-size: 30px;
    letter-spacing: 3px;
    fill: var(--silver);
  }
  .back-name-sub {
    font-family: "Cinzel", "Times New Roman", serif;
    font-weight: 400;
    font-size: 18px;
    letter-spacing: 5px;
    fill: var(--silver);
  }
</style>
</head>
<body>
  <section class="card card-front">
    <div class="front-brand">
      <span class="brand-dot"></span>
      <span class="brand-name">Harbor Vault Works</span>
    </div>
    <div class="front-divider"></div>
    <div class="contact">
      <div class="contact-name">Daniel Harper</div>
      <div class="contact-role">Managing Director</div>
      <div class="contact-address">12345, Address Goes Here<br>Country Name, 123456.</div>
      <div class="contact-line">
        <svg viewBox="0 0 10 10"><path d="M2 0.5l1.6 2-1 1.1a6 6 0 0 0 3.8 3.8l1.1-1 2 1.6-1 1.5C4.5 9.5 0.5 5.5 0.5 1.5z"/></svg>
        <span>044-987 654 321</span>
      </div>
      <div class="contact-line">
        <svg viewBox="0 0 10 10"><path d="M0 2h10v6H0z M0 2l5 3.5L10 2" stroke="#0f0f0f" stroke-width=".8"/></svg>
        <span>info@harborvault.com</span>
      </div>
      <div class="contact-line">
        <svg viewBox="0 0 10 10"><path d="M3.5 6.5l3-3" stroke="#e0201f" stroke-width="1.2"/><rect x="0.8" y="4.8" width="4" height="4" rx="2" fill="none" stroke="#e0201f" stroke-width="1.2"/><rect x="5.2" y="1.2" width="4" height="4" rx="2" fill="none" stroke="#e0201f" stroke-width="1.2"/></svg>
        <span>www.harborvault.com</span>
      </div>
    </div>
  </section>

  <section class="card card-back">
    <div class="back-lockup">
      <svg viewBox="0 0 520 300" aria-label="Harbor Vault Works">
        <defs>
          <path id="name-arch" d="M 100 158 Q 260 88 420 158" fill="none"/>
          <linearGradient id="scroll-tone" x1="0" x2="1" y1="0" y2="0">
            <stop offset="0" stop-color="#4a4a4a"/>
            <stop offset=".5" stop-color="#a8a8a8"/>
            <stop offset="1" stop-color="#4a4a4a"/>
          </linearGradient>
        </defs>
        <text class="back-name-arch" text-anchor="middle">
          <textPath href="#name-arch" startOffset="50%">HARBOR VAULT</textPath>
        </text>
        <text class="back-name-sub" x="260" y="186" text-anchor="middle">WORKS</text>
        <rect x="160" y="172" width="52" height="16" rx="8" fill="url(#scroll-tone)" opacity=".7" role="img" aria-label="Silver scroll flourish, left"/>
        <rect x="308" y="172" width="52" height="16" rx="8" fill="url(#scroll-tone)" opacity=".7" role="img" aria-label="Silver scroll flourish, right"/>
      </svg>
    </div>
  </section>
</body>
</html>
```